KWM Plumbing and Roofing

design a fresh modern card for a young plumbing business looking to break into the market.
Must include the logo in the attached file
Lowen Fairbrook
Phone number 0412689405
Vic Licence no 63920
email......

New Homes & Renovations
General Plumbing & Maintenance
Solar Hot Water Units
Roofing & Guttering (new and replacement)

Industry/Entity Type

Business

```html
<!DOCTYPE html>
<html lang="en">
<head>
<meta charset="UTF-8">
<title>KWM Plumbing and Roofing – Business Card</title>
<link rel="stylesheet" href="https://fonts.googleapis.com/css2?family=Montserrat:wght@400;500;600;700&display=swap">
<style>
  :root {
    --navy: #0d4472;
    --gold: #d7a531;
    --paper: #ffffff;
    --paper-shade: #f1f1f1;
    --backdrop: #e4e6e8;
  }
  * { box-sizing: border-box; margin: 0; padding: 0; }
  html, body {
    width: 1200px; height: 900px; overflow: hidden;
    background: var(--backdrop);
    font-family: "Montserrat", Arial, sans-serif;
  }
  .canvas {
    width: 1200px; height: 900px;
    display: flex; flex-direction: column; align-items: center; justify-content: center;
    gap: 40px;
  }
  .card {
    width: 700px; height: 400px;
    background: linear-gradient(160deg, var(--paper) 0%, var(--paper-shade) 100%);
    position: relative; overflow: hidden;
    box-shadow: 0 6px 18px rgba(0,0,0,.18);
  }

  /* brand name block */
  .brand { display: flex; align-items: center; gap: 16px; }
  .brand-dot { width: 44px; height: 44px; border-radius: 50%; background: var(--navy); flex: none; }
  .brand-name { color: var(--navy); font-weight: 700; line-height: 1.1; }

  /* front */
  .card-front .brand { position: absolute; left: 150px; top: 120px; }
  .card-front .brand-name { font-size: 34px; }
  .card-front .brand-name small { display: block; font-size: 22px; }
  .rule { position: absolute; left: 40px; right: 0; top: 292px; height: 1.5px; background: var(--navy); }
  .services {
    position: absolute; left: 40px; right: 24px; top: 308px;
    list-style: none; display: grid; grid-template-columns: auto 1fr; gap: 8px 20px;
    color: var(--navy); font-size: 12.5px; font-weight: 500; text-transform: uppercase; letter-spacing: .3px;
  }
  .services li { display: flex; align-items: center; gap: 6px; white-space: nowrap; }
  .tick { width: 12px; height: 12px; flex: none; }

  /* back */
  .card-back .brand { position: absolute; left: 30px; top: 168px; }
  .card-back .brand-dot { width: 34px; height: 34px; }
  .card-back .brand-name { font-size: 24px; }
  .card-back .brand-name small { display: block; font-size: 15px; }
  .panel { position: absolute; left: 300px; top: 0; width: 400px; height: 400px; }
  .details { position: absolute; left: 355px; top: 58px; color: #fff; }
  .person { color: var(--gold); font-size: 22px; font-weight: 600; letter-spacing: 1.6px; text-transform: uppercase; }
  .role { font-size: 12px; font-weight: 600; letter-spacing: 1.6px; margin-top: 6px; }
  .company { margin-top: 38px; color: var(--gold); font-size: 16px; font-weight: 500; letter-spacing: 1.6px; text-transform: uppercase; }
  .licence, .address { font-size: 15px; letter-spacing: 1.3px; line-height: 1.45; }
  .address { margin-top: 14px; }
  .contacts { list-style: none; margin-top: 16px; font-size: 13.5px; letter-spacing: 1px; }
  .contacts li { display: flex; align-items: center; gap: 14px; line-height: 1.65; }
  .contacts .phone { font-size: 15.5px; }
  .contact-icon { width: 15px; height: 15px; border-radius: 3px; background: var(--gold); flex: none; display: flex; align-items: center; justify-content: center; }
  .contact-icon svg { width: 11px; height: 11px; }
  .upper { text-transform: uppercase; }
</style>
</head>
<body>
<main class="canvas">

  <section class="card card-front" aria-label="Card front">
    <div class="brand">
      <span class="brand-dot"></span>
      <div class="brand-name">KWM <small>Plumbing and Roofing</small></div>
    </div>
    <div class="rule"></div>
    <ul class="services">
      <li><svg class="tick" viewBox="0 0 12 12"><path d="M1 6.5l3 3 7-8" fill="none" stroke="#d7a531" stroke-width="2"/></svg>New Homes &amp; Renovations</li>
      <li><svg class="tick" viewBox="0 0 12 12"><path d="M1 6.5l3 3 7-8" fill="none" stroke="#d7a531" stroke-width="2"/></svg>General Plumbing &amp; Maintenance</li>
      <li><svg class="tick" viewBox="0 0 12 12"><path d="M1 6.5l3 3 7-8" fill="none" stroke="#d7a531" stroke-width="2"/></svg>Solar Hot Water Units</li>
      <li><svg class="tick" viewBox="0 0 12 12"><path d="M1 6.5l3 3 7-8" fill="none" stroke="#d7a531" stroke-width="2"/></svg>Roofing &amp; Guttering (New and Replacement)</li>
    </ul>
  </section>

  <section class="card card-back" aria-label="Card back">
    <div class="brand">
      <span class="brand-dot"></span>
      <div class="brand-name">KWM <small>Plumbing and Roofing</small></div>
    </div>
    <svg class="panel" viewBox="0 0 400 400" preserveAspectRatio="none" aria-hidden="true">
      <polygon points="0,0 400,0 400,400 50,400 40,260 40,145 55,125 38,105" fill="#d7a531"/>
      <polygon points="10,0 400,0 400,400 62,400 52,260 52,145 67,125 48,105" fill="#0d4472"/>
    </svg>
    <div class="details">
      <p class="person">Marcus Hale</p>
      <p class="role">PRESIDENT</p>
      <p class="company">Lowen Fairbrook</p>
      <p class="licence">Vic Licence no 63920</p>
      <p class="address">42 Harbour View Rd<br>Geelong, VIC 3220</p>
      <ul class="contacts">
        <li class="phone"><span class="contact-icon"><svg viewBox="0 0 12 12"><rect x="3" y="1" width="6" height="10" rx="1" fill="none" stroke="#0d4472" stroke-width="1.4"/></svg></span><span>041-268-9405</span></li>
        <li><span class="contact-icon"><svg viewBox="0 0 12 12"><rect x="1" y="2.5" width="10" height="7" fill="none" stroke="#0d4472" stroke-width="1.3"/><path d="M1 3l5 4 5-4" fill="none" stroke="#0d4472" stroke-width="1.3"/></svg></span><span>info@<span class="upper">lowenfairbrook.com</span></span></li>
        <li><span class="contact-icon"><svg viewBox="0 0 12 12"><circle cx="6" cy="6" r="4.6" fill="none" stroke="#0d4472" stroke-width="1.2"/><path d="M1.5 6h9M6 1.4c-2.4 3-2.4 6.2 0 9.2M6 1.4c2.4 3 2.4 6.2 0 9.2" fill="none" stroke="#0d4472" stroke-width="1"/></svg></span><span class="upper">www.lowenfairbrook.com</span></li>
      </ul>
    </div>
  </section>

</main>
</body>
</html>
```